Pelton Mortgage Capital Business Card

We need a business card design for our mortgage servicing company. In addition to servicing the loans of homeowners, we help homeowners with purchasing their homes and any mortgage refinancing. We would like to see designs that use the colors in the logo attached below (gold-ish yellow and navy blue), and any other design you deem fit! The design should communicate a simpler life with smart mortgages provided by Pelton.

```html
<!DOCTYPE html>
<html lang="en">
<head>
<meta charset="utf-8">
<title>Pelton Mortgage Capital Business Card</title>
<link href="https://fonts.googleapis.com/css2?family=Open+Sans:wght@400;600;700&display=swap" rel="stylesheet">
<style>
  :root {
    --navy: #262255;
    --gold: #e0b03a;
    --paper: #ffffff;
    --ink: #2b2b2b;
    --stage: #3a3a3a;
  }
  * { margin: 0; padding: 0; box-sizing: border-box; }
  html, body { width: 1200px; height: 689px; overflow: hidden; }
  body {
    background: var(--stage);
    font-family: "Open Sans", Arial, sans-serif;
    position: relative;
  }
  .card {
    position: absolute;
    top: 194px;
    width: 520px;
    height: 300px;
    background: var(--paper);
    border-radius: 22px;
    overflow: hidden;
  }
  .card--front { left: 45px; }
  .card--back { left: 635px; }

  .wordmark {
    position: absolute;
    left: 0; right: 0;
    display: flex;
    align-items: center;
    justify-content: center;
    gap: 12px;
    color: var(--navy);
    font-weight: 700;
    letter-spacing: 0.5px;
  }
  .wordmark__dot {
    width: 18px; height: 18px;
    border-radius: 50%;
    background: var(--gold);
  }
  .card--front .wordmark { top: 128px; font-size: 38px; }
  .card--back .wordmark { top: 62px; font-size: 34px; }

  .person {
    position: absolute;
    left: 40px;
    top: 168px;
    width: 200px;
    text-align: right;
    color: var(--ink);
    font-size: 12.5px;
    line-height: 1.45;
  }
  .person__name {
    color: var(--gold);
    font-weight: 700;
    font-size: 20px;
    letter-spacing: 0.5px;
    line-height: 1.2;
    margin-bottom: 2px;
  }
  .divider {
    position: absolute;
    left: 256px;
    top: 160px;
    width: 1.5px;
    height: 86px;
    background: var(--gold);
  }
  .contacts {
    position: absolute;
    left: 274px;
    top: 168px;
    list-style: none;
    color: var(--ink);
    font-size: 12.5px;
    line-height: 1.5;
  }
  .contacts li { display: flex; align-items: center; gap: 8px; margin-bottom: 3px; }
  .contacts svg { width: 12px; height: 12px; fill: var(--gold); flex: none; }

  .band--navy {
    position: absolute;
    left: 0; bottom: 0;
    width: 56%;
    height: 8px;
    background: var(--navy);
  }
  .band--gold {
    position: absolute;
    right: 0; bottom: 0;
    width: 44%;
    height: 16px;
    background: var(--gold);
  }
</style>
</head>
<body>
  <section class="card card--front" aria-label="Card front">
    <div class="wordmark"><span class="wordmark__dot"></span><span>Pelton Mortgage</span></div>
  </section>

  <section class="card card--back" aria-label="Card back">
    <div class="wordmark"><span class="wordmark__dot"></span><span>Pelton Mortgage</span></div>

    <div class="person">
      <p class="person__name">DANA BROOKS</p>
      <p>Managing Director</p>
      <p>Your address, City</p>
      <p>State, Zip 1234</p>
    </div>

    <div class="divider"></div>

    <ul class="contacts">
      <li>
        <svg viewBox="0 0 24 24" aria-hidden="true"><path d="M6.6 10.8a15.1 15.1 0 0 0 6.6 6.6l2.2-2.2a1 1 0 0 1 1-.25 11.4 11.4 0 0 0 3.6.57 1 1 0 0 1 1 1V20a1 1 0 0 1-1 1A17 17 0 0 1 3 4a1 1 0 0 1 1-1h3.5a1 1 0 0 1 1 1c0 1.25.2 2.45.57 3.57a1 1 0 0 1-.25 1z"/></svg>
        <span>123 456 789</span>
      </li>
      <li>
        <svg viewBox="0 0 24 24" aria-hidden="true"><path d="M2 5h20v14H2z M2 5l10 8 10-8" /></svg>
        <span>info@peltonmail.com</span>
      </li>
      <li>
        <svg viewBox="0 0 24 24" aria-hidden="true"><circle cx="12" cy="12" r="10"/></svg>
        <span>www.peltonmortgage.com</span>
      </li>
    </ul>

    <div class="band--navy"></div>
    <div class="band--gold"></div>
  </section>
</body>
</html>
```